Vintage home page design (Bellweather Coupes and Wagons - 7815)

Wants a vintage-themed website.
http://www.bellweathercoupeshub.com/
Likes the retro graphics used on this site (the signs and the cartoon at the bottom of the boy holding the flag)

Client is open to a light or dark background, and wants to see what you come up with. Use their logo colors as accent colors throughout the home page design.
Keep it retro and vintage and have fun!

Attached their logo and a .psd layout example. The layout example is just for referencing the dimensions we usually use, but it's not set in stone.

Let me know if you have any questions and I'll answer them as soon as possible.

Thank you designers for your early submissions! I am waiting to hear back from the client and will keep each of you updated when they reply. Best regards, Maribel

Hello everyone- Thanks so much for being patient, I am still waiting to hear back from the client and get feedback. I just sent another follow up email and will let you all know when I get feedback. Best regards, Maribel

```html
<!DOCTYPE html>
<html lang="en">
<head>
<meta charset="utf-8">
<title>Bellweather Coupes and Wagons</title>
<link rel="stylesheet" href="https://fonts.googleapis.com/css2?family=Rye&family=Lora:wght@400;700&display=swap">
<style>
  :root {
    --paper: #f2e7c6;
    --paper-dark: #e6d6a8;
    --footer: #dcc38e;
    --footer-edge: #cfb47c;
    --navy: #1f2a78;
    --red: #d21f28;
    --ink: #4a3b2c;
    --nav-ink: #3d3a44;
    --rule: #cdbb93;
    --gold: #c9a763;
    --field: #efe3c0;
    --field-line: #d6c59c;
    --frame: #fbf6ea;
  }
  * { box-sizing: border-box; margin: 0; padding: 0; }
  html, body { width: 853px; height: 1200px; overflow: hidden; background: var(--paper); }
  .page {
    position: relative; width: 853px; height: 1200px; overflow: hidden;
    background: radial-gradient(ellipse at 50% 40%, #f5ebcd 0%, var(--paper) 55%, var(--paper-dark) 100%);
    font-family: 'Lora', Georgia, serif; color: var(--ink);
  }
  .brand {
    position: absolute; left: 0; top: 28px; width: 853px; text-align: center;
    font-family: 'Rye', serif; color: var(--navy); font-size: 22px; line-height: 28px;
  }
  .main-nav {
    position: absolute; left: 116px; top: 128px; width: 622px; height: 31px;
    border-top: 1px solid var(--rule); border-bottom: 1px solid var(--rule);
  }
  .main-nav a {
    position: absolute; top: 8px; font-family: 'Rye', serif; font-size: 12.5px;
    color: var(--nav-ink); text-decoration: none; text-transform: uppercase; letter-spacing: .5px;
  }
  .slider-tab { position: absolute; top: 282px; width: 20px; height: 70px; border: 1px solid var(--rule); border-radius: 10px; }
  .slider-tab.left { left: 90px; }
  .slider-tab.right { left: 744px; }
  .slider-arrow { position: absolute; left: 747px; top: 310px; }
  .hero {
    position: absolute; left: 116px; top: 178px; width: 620px; height: 279px;
    background: var(--frame); border-radius: 8px; padding: 5px;
    box-shadow: 0 1px 4px rgba(90,70,40,.35);
  }
  .hero-photo {
    width: 100%; height: 100%; border-radius: 4px;
    background: linear-gradient(180deg, #b9cbe8 0%, #d8e2f0 38%, #7d6c62 46%, #ddd5c6 55%, #cfc6b8 100%);
  }
  .welcome { position: absolute; left: 0; top: 508px; width: 853px; text-align: center; }
  .welcome .kicker { font-family: 'Rye', serif; color: var(--navy); font-size: 17px; }
  .welcome h1 { font-family: 'Rye', serif; color: var(--red); font-size: 29px; font-weight: 400; line-height: 34px; text-transform: uppercase; }
  .welcome-rule { position: absolute; left: 376px; width: 100px; height: 1px; background: var(--rule); }
  .intro {
    position: absolute; left: 118px; top: 608px; width: 618px; text-align: center;
    font-size: 8.6px; line-height: 14.5px; color: var(--ink);
  }
  .intro p { margin-bottom: 4px; }
  .section-rule { position: absolute; left: 116px; width: 622px; height: 1px; background: var(--rule); }
  .features-title {
    position: absolute; left: 0; top: 750px; width: 853px; text-align: center;
    font-family: 'Rye', serif; color: var(--navy); font-size: 20px; text-transform: uppercase;
  }
  .vehicle {
    position: absolute; top: 806px; width: 142px; height: 97px; border-radius: 22px;
    background: var(--frame); padding: 4px; box-shadow: 0 1px 3px rgba(90,70,40,.4);
  }
  .vehicle div { width: 100%; height: 100%; border-radius: 18px; }
  .carousel-arrow { position: absolute; top: 846px; }
  .contact-title { position: absolute; left: 115px; top: 944px; font-family: 'Rye', serif; color: var(--navy); font-size: 18px; text-transform: uppercase; }
  .field {
    position: absolute; background: var(--field); border: 1px solid var(--field-line); border-radius: 3px;
    font-size: 8.5px; color: #8a7a62; padding: 5px 7px;
  }
  .send-button {
    position: absolute; left: 420px; top: 1006px; width: 60px; height: 22px; border-radius: 3px;
    background: var(--gold); color: #fff; font-size: 11.5px; font-weight: 700; text-align: center; line-height: 22px;
  }
  .footer { position: absolute; left: 0; top: 1052px; width: 853px; height: 148px; background: var(--footer); border-top: 3px solid var(--footer-edge); }
  .footer-line { position: absolute; left: 132px; display: flex; align-items: flex-start; gap: 9px; font-size: 9.5px; color: #2f2a24; line-height: 13px; }
  .footer-line.phone { font-size: 13px; }
  .footer-line.email { color: var(--red); font-size: 8.6px; }
  .footer-links { position: absolute; left: 114px; top: 1174px; font-size: 7.5px; color: #2f2a24; }
  .mascot { position: absolute; left: 350px; top: 1062px; width: 150px; height: 126px; border-radius: 6px; background: linear-gradient(180deg, #efe6d2, #d7c49a); }
  .hours {
    position: absolute; left: 543px; top: 1080px; width: 194px; height: 84px;
    border: 4px solid #c8b690; border-radius: 6px; background: #e9dcb8; text-align: center; padding-top: 18px;
  }
  .hours h2 { font-family: 'Lora', serif; font-weight: 400; font-size: 11px; text-transform: uppercase; color: #2f2a24; margin-bottom: 6px; }
  .hours p { font-size: 9.5px; color: #b0631b; line-height: 13px; }
  .hours .accent { color: var(--red); }
  .social { position: absolute; top: 1156px; width: 11px; height: 11px; border-radius: 2px; background: #b59c73; }
  .copyright { position: absolute; left: 522px; top: 1174px; font-size: 7.5px; color: #2f2a24; }
</style>
</head>
<body>
<div class="page">
  <div class="brand">Bellweather Coupes<br>and Wagons</div>

  <nav class="main-nav">
    <a style="left:22px">Home</a>
    <a style="left:95px">Inventory</a>
    <a style="left:197px">About Us</a>
    <a style="left:294px">Sell Your Classic</a>
    <a style="left:442px">Contact Us</a>
    <a style="left:550px">VIP List</a>
  </nav>

  <div class="slider-tab left"></div>
  <div class="slider-tab right"></div>
  <div class="hero"><div class="hero-photo" role="img" aria-label="Vintage black sedan with an American flag parked in a desert landscape"></div></div>
  <svg class="slider-arrow" width="12" height="16" viewBox="0 0 12 16"><path d="M3 2l6 6-6 6" fill="none" stroke="#111" stroke-width="2"/></svg>

  <div class="welcome-rule" style="top:494px"></div>
  <div class="welcome">
    <div class="kicker">WELCOME TO</div>
    <h1>Bellweather Coupes and Wagons</h1>
  </div>
  <div class="welcome-rule" style="top:586px"></div>

  <div class="intro">
    <p>Lorem Ipsum is simply dummy text of the printing and typesetting industry. Lorem Ipsum has been the industry's standard dummy text ever since the 1500s, when an unknown printer took a galley of type and scrambled it to make a type specimen book.</p>
    <p>It has survived not only five centuries, but also the leap into electronic typesetting, remaining essentially unchanged.</p>
    <p>It was popularised in the 1960s with the release of Letraset sheets containing Lorem Ipsum passages, and more recently with desktop publishing software like Aldus PageMaker including versions of Lorem Ipsum. It is a long established fact that a reader will be distracted by the readable content of a page when looking at its layout.</p>
  </div>

  <div class="section-rule" style="top:745px"></div>
  <div class="features-title">Features Vehicles</div>
  <div class="section-rule" style="top:776px"></div>

  <svg class="carousel-arrow" style="left:92px" width="18" height="12" viewBox="0 0 18 12"><path d="M17 6H3M8 1L3 6l5 5" fill="none" stroke="#6b5a45" stroke-width="1.5"/></svg>
  <div class="vehicle" style="left:116px"><div role="img" aria-label="White classic sedan" style="background:linear-gradient(180deg,#f4f1ea,#c9c2b6)"></div></div>
  <div class="vehicle" style="left:276px"><div role="img" aria-label="Blue vintage car in front of a timber house" style="background:linear-gradient(180deg,#b79a82,#4f8db3 60%,#7c7a6a)"></div></div>
  <div class="vehicle" style="left:436px"><div role="img" aria-label="Black vintage sedan with flag" style="background:linear-gradient(180deg,#c9d8ea,#3b352e 60%,#bfb39c)"></div></div>
  <div class="vehicle" style="left:596px"><div role="img" aria-label="Cream classic sedan" style="background:linear-gradient(180deg,#ffffff,#e6dcc8)"></div></div>
  <svg class="carousel-arrow" style="left:743px" width="18" height="12" viewBox="0 0 18 12"><path d="M1 6h14M10 1l5 5-5 5" fill="none" stroke="#6b5a45" stroke-width="1.5"/></svg>

  <div class="contact-title">Contact Us</div>
  <div class="field" style="left:258px;top:947px;width:156px;height:21px">Name</div>
  <div class="field" style="left:258px;top:976px;width:156px;height:21px">Email address</div>
  <div class="field" style="left:258px;top:1006px;width:156px;height:21px">Phone no</div>
  <div class="field" style="left:420px;top:947px;width:317px;height:50px">Message</div>
  <div class="send-button">Send</div>

  <footer class="footer"></footer>
  <div class="footer-line" style="top:1086px">
    <svg width="9" height="12" viewBox="0 0 9 12"><path d="M4.5 0A4.5 4.5 0 0 0 0 4.5C0 8 4.5 12 4.5 12S9 8 9 4.5A4.5 4.5 0 0 0 4.5 0z" fill="#5a4d3e"/><circle cx="4.5" cy="4.5" r="1.7" fill="#dcc38e"/></svg>
    <span>502, Lorem Ipsum Street, Country name,<br>Zip code 012345</span>
  </div>
  <div class="footer-line phone" style="top:1119px">
    <svg width="11" height="10" viewBox="0 0 11 10"><path d="M1 3c0-2 9-2 9 0v1H7V3H4v1H1z M2 5h7l1 4H1z" fill="#5a4d3e"/></svg>
    <span>+0123 555 019</span>
  </div>
  <div class="footer-line email" style="top:1146px">
    <svg width="10" height="8" viewBox="0 0 10 8"><rect width="10" height="8" fill="#5a4d3e"/><path d="M0 0l5 4 5-4" fill="none" stroke="#dcc38e"/></svg>
    <span>info@bellweathercoupes.example</span>
  </div>
  <div class="footer-links">Home | Inventory | About Us | Sell Your Classic | Contact Us | VIP List</div>

  <div class="mascot" role="img" aria-label="Retro cartoon mascot holding a best services guarantee badge"></div>

  <div class="hours">
    <h2>Hours of Operation</h2>
    <p>Monday to Saturday : <span>By Appointment</span></p>
    <p>Sunday : <span class="accent">Closed</span></p>
  </div>
  <div class="social" style="left:616px"></div>
  <div class="social" style="left:634px"></div>
  <div class="social" style="left:652px"></div>
  <div class="copyright">Copyright ©2014 Bellweather Coupes and Wagons. All Rights Reserved.</div>
</div>
</body>
</html>
```